Business Card Design for RT Wine:

I'm looking for a card that has the following.
Front:
- Merlot Colored
- stripe down the middle in silver or gold flake
- RT in block like thick letters with gold or silver flake above stripe
-Wine: below stripe
- a grape bunch that is at the end of the stripe that is made so it can be printed as embossed
Back:
- line down the middle of card in Merlot, card is white background
- to the left Marisa Dobbs, (next line) Owner, (next line) Certified Sommelier, BPL
- to the right (listed) restaurant consulting, wine tours, personal tastings, event planning, personal wine buying
- add embossed grape bunch
Also, looking for a piece that slides over like a envelope for a room key for a hotel that says "We met @ VANDORA" and possibly a file for that, that I can edit.
Would like card to be printed on a thicker cardstock

```html
<!DOCTYPE html>
<html lang="en">
<head>
<meta charset="utf-8">
<title>RT Wine – Business Card</title>
<link rel="stylesheet" href="https://fonts.googleapis.com/css2?family=Oswald:wght@700&family=Arimo:wght@400;700&display=swap">
<style>
  :root {
    --backdrop: #ebe8e4;
    --merlot: #4f2a33;
    --gold: #b8924a;
    --silver-light: #e6e6e6;
    --silver-mid: #bdbdbd;
    --silver-dark: #9a9a9a;
    --paper: #ffffff;
    --ink: #111111;
    --wine-label: #e4dfe0;
    --grape-tone: #d9d9d9;
    --grape-tone-dark: #cfcfcf;
  }
  * { box-sizing: border-box; margin: 0; padding: 0; }
  html, body {
    width: 1200px; height: 1000px; overflow: hidden;
    background: var(--backdrop);
    font-family: "Arimo", Arial, sans-serif;
  }
  .sheet {
    width: 1200px; height: 1000px;
    display: flex; flex-direction: column; align-items: center; justify-content: center;
    gap: 60px;
  }
  .card {
    position: relative;
    width: 700px; height: 400px;
    box-shadow: 0 6px 18px rgba(0,0,0,0.15);
    overflow: hidden;
  }

  /* Back side */
  .card-back { background: var(--paper); color: var(--ink); }
  .card-back .identity {
    position: absolute; left: 34px; top: 150px; width: 290px;
  }
  .card-back .name {
    font-family: "Oswald", "Arial Narrow", sans-serif;
    font-weight: 700; font-size: 40px; line-height: 1.1;
    text-transform: uppercase; letter-spacing: 0.5px;
  }
  .card-back .role { font-size: 38px; line-height: 1.2; margin-top: 4px; }
  .card-back .credential { font-size: 25px; margin-top: 22px; white-space: nowrap; }
  .card-back .divider {
    position: absolute; left: 340px; top: 28px; bottom: 28px;
    width: 2px; background: var(--merlot);
  }
  .card-back .services {
    position: absolute; left: 362px; top: 34px;
    list-style: none; font-size: 27px; line-height: 1.3;
  }
  .card-back .grape-emboss {
    position: absolute; right: 52px; bottom: 70px; width: 90px; height: 105px;
    border-radius: 45% 45% 50% 50%;
    background: radial-gradient(circle at 45% 40%, #f2f2f2, var(--grape-tone-dark));
  }

  /* Front side */
  .card-front { background: var(--merlot); }
  .card-front .monogram {
    position: absolute; left: 0; right: 0; top: 26px;
    text-align: center;
    font-weight: 700; font-size: 112px; line-height: 1; letter-spacing: 2px;
    color: var(--gold);
  }
  .card-front .stripe {
    position: absolute; left: 0; right: 0; top: 162px; height: 56px;
    background: linear-gradient(180deg, var(--silver-dark) 0%, var(--silver-light) 30%, var(--silver-mid) 60%, var(--silver-light) 85%, var(--silver-dark) 100%);
  }
  .card-front .tagline {
    position: absolute; left: 42px; top: 236px;
    font-size: 34px; letter-spacing: 1px; color: var(--wine-label);
  }
  .card-front .grape-emboss {
    position: absolute; right: 28px; top: 130px; width: 110px; height: 120px;
    border-radius: 45% 45% 50% 50%;
    background: radial-gradient(circle at 45% 40%, #efe9ea, var(--grape-tone));
    opacity: 0.85;
  }
</style>
</head>
<body>
  <main class="sheet">
    <section class="card card-back">
      <div class="identity">
        <p class="name">Marisa Dobbs</p>
        <p class="role">Owner</p>
        <p class="credential">Certified Sommelier, BPL</p>
      </div>
      <div class="divider"></div>
      <ul class="services">
        <li>Restaurant Consulting,</li>
        <li>Wine Tours,</li>
        <li>Personal Tastings,</li>
        <li>Event Planning,</li>
        <li>Personal Wine</li>
        <li>Buying</li>
      </ul>
      <div class="grape-emboss" role="img" aria-label="Embossed grape bunch line illustration"></div>
    </section>

    <section class="card card-front">
      <p class="monogram">RT</p>
      <div class="stripe"></div>
      <div class="grape-emboss" role="img" aria-label="Embossed grape bunch line illustration at the end of the stripe"></div>
      <p class="tagline">WINE</p>
    </section>
  </main>
</body>
</html>
```